Faithful in the Small...Powerful together

Capital Campaign for Brightwell Chapel...need it engaging..spiritually based with pics of the community etc...

Target Market(s)

church congregation and sphere of influence

Industry/Entity Type

religious

Colors
EB3D1F
EC4F4E
F09395
F8D3D4
FCEDEE

Requirements
Must have
• tier levels..engaging scripture and photos

```html
<!DOCTYPE html>
<html lang="en">
<head>
<meta charset="utf-8">
<title>Brightwell Chapel – Faithful in the Small, Powerful Together</title>
<link rel="stylesheet" href="https://fonts.googleapis.com/css2?family=Great+Vibes&family=Libre+Baskerville:ital,wght@1,400;1,700&family=Roboto:ital,wght@0,400;0,500;0,700;0,900;1,400&display=swap">
<style>
:root{
  --board:#8f8f8f;
  --red-deep:#8a1a1e;
  --red-panel:#a32327;
  --red:#c0202a;
  --red-bright:#eb3d1f;
  --red-soft:#ec4f4e;
  --pink:#f09395;
  --pink-pale:#f8d3d4;
  --pink-mist:#fcedee;
  --ink:#1a1a1a;
  --grey:#6c6c6c;
  --white:#ffffff;
}
*{margin:0;padding:0;box-sizing:border-box}
html,body{width:1200px;height:787px;overflow:hidden}
body{background:var(--board);font-family:"Roboto",Arial,sans-serif;position:relative;color:var(--ink)}
.side-label{position:absolute;top:33px;font:700 16px/1 "Roboto",sans-serif;letter-spacing:4px;color:var(--white);transform:translateX(-50%)}
.page{position:absolute;overflow:hidden;background:var(--white)}
.page--front{left:53px;top:58px;width:526px;height:680px}
.page--back{left:617px;top:58px;width:524px;height:678px}
.layer{position:absolute;left:0;top:0}
.abs{position:absolute}
.script{font-family:"Great Vibes",cursive;font-weight:400}

/* front */
.campaign-title{left:42px;top:18px;font-size:29px;color:var(--white);white-space:nowrap}
.goal-pill{left:40px;top:61px;width:260px;height:27px;border-radius:14px;background:var(--red);color:var(--white);font:700 16px/27px "Roboto",sans-serif;text-align:center}
.facts{left:41px;top:99px;list-style:none;color:var(--white);font-size:12px;line-height:14px}
.facts li,.vision-points li{display:flex;align-items:center;gap:5px}
.tick{width:10px;height:9px;flex:none}
.per-person{left:42px;top:154px;color:var(--white);font-size:16px;line-height:18px}
.per-person strong{font-weight:700}
.seal{width:150px;height:150px;border-radius:50%;background:var(--red-deep);display:flex;align-items:center;justify-content:center}
.seal__inner{width:132px;height:132px;border-radius:50%;background:var(--white);display:flex;align-items:center;justify-content:center;text-align:center;font:700 18px/1.1 "Roboto",sans-serif;color:var(--ink)}
.seal--front{left:35px;top:208px}
.vision-kicker{left:40px;top:366px;font-size:27px;color:var(--red);line-height:1}
.vision-title{left:43px;top:395px;font:700 20px/1 "Roboto",sans-serif;color:var(--red)}
.vision-points{left:38px;top:427px;list-style:none;font-size:12px;line-height:14px;color:var(--ink)}
.verse{left:40px;width:215px;height:51px;border:1px solid var(--red);border-radius:9px}
.verse--one{top:495px}.verse--two{top:572px}
.verse__marks{position:absolute;left:14px;top:-14px;display:flex;gap:4px}
.verse__mark{width:22px;height:22px;border-radius:50%;background:var(--red);color:var(--white);font:700 20px/30px "Libre Baskerville",serif;text-align:center}
.verse__text{position:absolute;left:16px;top:13px;font:italic 700 10.5px/12.5px "Libre Baskerville",serif;color:var(--ink)}
.verse__ref{position:absolute;left:13px;bottom:-7px;padding:0 4px;background:#f8f8f8;font:italic 700 10px/1 "Libre Baskerville",serif;color:var(--red)}
.motto{text-align:center;color:var(--red);width:100px}
.motto__word{font-size:48px;line-height:1}
.motto__tail{display:block;font-size:15px;line-height:1;margin-top:-10px}
.motto--love{left:278px;top:498px}
.motto--live{left:397px;top:498px}
.motto--lead{left:338px;top:570px}
.motto-rule-v{left:384px;top:506px;width:1px;height:56px;background:#bbb}
.motto-rule-h{left:276px;top:566px;width:215px;height:1px;background:#bbb}
.site-front{left:0;width:100%;top:663px;text-align:center;color:var(--white);font-size:10.5px}

/* back */
.kicker{font-size:24px;color:var(--white);line-height:1}
.heading{font:700 15px/1 "Roboto",sans-serif;color:var(--white)}
.body-copy{font-size:7.2px;line-height:9px;color:var(--white)}
.stories-kicker{left:51px;top:32px}
.stories-title{left:51px;top:57px}
.stories-copy{left:51px;top:86px;width:210px}
.stories-copy p{margin-bottom:8px}
.stories-copy em{font-size:8px;line-height:10px;display:block}
.dotted{left:51px;width:202px;border-top:1.5px dashed rgba(255,255,255,.6)}
.join{left:51px;top:236px;width:202px;text-align:center;font:900 38px/1 "Roboto",sans-serif;color:var(--white)}
.practice{top:291px;width:40px;text-align:center;color:var(--white);font:500 9px/1 "Roboto",sans-serif}
.practice__ring{width:37px;height:37px;border:1.3px solid var(--white);border-radius:50%;margin:0 auto 6px;display:flex;align-items:center;justify-content:center}
.belief{left:51px;top:347px;width:202px;text-align:center;font:italic 8px/10px "Roboto",sans-serif;color:var(--white)}
.forward-kicker{left:300px;top:32px}
.forward-title{left:300px;top:55px}
.encourage{left:300px;top:80px;width:200px}
.encourage b{display:block;font-size:9px;line-height:11px;margin-bottom:2px}
.shared-kicker{left:300px;top:146px}
.shared-title{left:300px;top:170px}
.shared-copy{left:300px;top:195px;width:200px}
.seal--back{left:346px;top:250px;width:140px;height:140px}
.seal--back .seal__inner{width:124px;height:124px}
.model-title{left:42px;top:433px;font:700 20px/1 "Roboto",sans-serif;color:var(--ink)}
.model-sub{left:43px;top:460px;font:italic 12px/1 "Roboto",sans-serif;color:var(--grey)}
.tier-title{left:42px;top:487px;font:700 12.5px/1 "Roboto",sans-serif;color:var(--red)}
.tiers{left:43px;top:508px;width:333px;border-collapse:collapse;font-size:8.5px;background:var(--white)}
.tiers th{height:19px;text-align:left;padding-left:9px;color:var(--white);font:500 11px/1 "Roboto",sans-serif;background:#1d1d1d}
.tiers th:first-child{background:var(--red)}
.tiers td{padding:0 9px;border-bottom:1px solid #ddd;color:#333;line-height:10px}
.tiers td:nth-child(1),.tiers td:nth-child(3){background:var(--pink-mist)}
.tiers tr:nth-child(1) td{height:34px}.tiers tr:nth-child(2) td{height:24px}
.tiers tr:nth-child(3) td{height:32px}.tiers tr:nth-child(4) td{height:30px}
.tiers col.c1{width:70px}.tiers col.c2{width:74px}.tiers col.c3{width:96px}
.total{left:394px;top:506px;font:700 13px/1 "Roboto",sans-serif;color:var(--red-bright)}
.total-note{left:394px;top:524px;width:120px;font-size:10px;line-height:12px;color:var(--grey)}
.margins{left:394px;top:561px;list-style:none;font-size:9.5px;line-height:13px;color:var(--ink)}
.margins li::before{content:"";display:inline-block;width:4px;height:4px;border-radius:50%;background:var(--ink);margin-right:4px;vertical-align:middle}
.rule-set{left:394px;top:628px;display:flex;gap:2px}
.rule-set span{width:23px;height:2px;background:var(--red)}
.rule-set span:nth-child(2){background:var(--ink)}
.site-back{left:394px;top:638px;font-size:9.5px;color:var(--red)}
</style>
</head>
<body>
<span class="side-label" style="left:315px">FRONT</span>
<span class="side-label" style="left:886px">BACK</span>

<!-- FRONT PAGE -->
<section class="page page--front">
  <svg class="layer" width="526" height="680" viewBox="0 0 526 680" aria-hidden="true">
    <defs>
      <radialGradient id="mist" cx="50%" cy="60%" r="70%"><stop offset="0" stop-color="#ffffff"/><stop offset="1" stop-color="#e9e9e9"/></radialGradient>
      <linearGradient id="swoosh" x1="0" x2="1"><stop offset="0" stop-color="#c0181a"/><stop offset=".6" stop-color="#ec4f4e"/><stop offset="1" stop-color="#f8d3d4"/></linearGradient>
    </defs>
    <rect width="526" height="680" fill="url(#mist)"/>
    <path d="M60 680 Q265 625 470 680 Z" fill="var(--red-deep)"/>
  </svg>
  <svg class="layer" width="526" height="310" viewBox="0 0 526 310" role="img" aria-label="Photo: two members of the congregation embracing inside the church">
    <defs><linearGradient id="hug" x1="0" y1="0" x2="1" y2="1"><stop offset="0" stop-color="#141212"/><stop offset=".55" stop-color="#3d3530"/><stop offset="1" stop-color="#6d6258"/></linearGradient></defs>
    <path d="M0 0H526V263C490 235 450 222 400 226C330 232 270 262 200 290C150 308 60 310 0 288Z" fill="url(#hug)"/>
  </svg>
  <svg class="layer" width="526" height="330" viewBox="0 0 526 330" aria-hidden="true">
    <path d="M175 308C260 290 330 240 410 228C460 222 500 232 526 250" fill="none" stroke="url(#swoosh)" stroke-width="7" stroke-linecap="round"/>
  </svg>

  <h1 class="abs script campaign-title">Faithful in the Small, Powerful Together</h1>
  <div class="abs goal-pill">Goal: $150,000 in 12 Months</div>
  <ul class="abs facts">
    <li><svg class="tick" viewBox="0 0 10 9"><path d="M1 5l3 3 5-7" fill="none" stroke="#eb3d1f" stroke-width="2"/></svg><span><strong>Total Goal:</strong> $150,000</span></li>
    <li><svg class="tick" viewBox="0 0 10 9"><path d="M1 5l3 3 5-7" fill="none" stroke="#eb3d1f" stroke-width="2"/></svg><span><strong>Active Members:</strong> approximately 150 people</span></li>
    <li><svg class="tick" viewBox="0 0 10 9"><path d="M1 5l3 3 5-7" fill="none" stroke="#eb3d1f" stroke-width="2"/></svg><span><strong>Timeframe:</strong> 12 months</span></li>
  </ul>
  <p class="abs per-person"><strong>That is $1,000 per person</strong><br>per year on average</p>

  <div class="abs seal seal--front"><div class="seal__inner">Brightwell<br>Chapel</div></div>

  <p class="abs script vision-kicker">The Heart</p>
  <h2 class="abs vision-title">of the Vision</h2>
  <ul class="abs vision-points">
    <li><svg class="tick" viewBox="0 0 10 9"><path d="M1 5l3 3 5-7" fill="none" stroke="#eb3d1f" stroke-width="2"/></svg>We are restoring more than space.</li>
    <li><svg class="tick" viewBox="0 0 10 9"><path d="M1 5l3 3 5-7" fill="none" stroke="#eb3d1f" stroke-width="2"/></svg>We are restoring a church where we</li>
  </ul>

  <figure class="abs verse verse--one">
    <div class="verse__marks"><span class="verse__mark">“</span><span class="verse__mark">”</span></div>
    <blockquote class="verse__text">Whoever is faithful in very little is<br>also faithful in much.</blockquote>
    <figcaption class="verse__ref">Luke 16:10</figcaption>
  </figure>
  <figure class="abs verse verse--two">
    <div class="verse__marks"><span class="verse__mark">“</span><span class="verse__mark">”</span></div>
    <blockquote class="verse__text">How good and pleasant it is when<br>God’s people live together in unity.</blockquote>
    <figcaption class="verse__ref">Psalm 133:1</figcaption>
  </figure>

  <svg class="abs" style="left:260px;top:287px" width="251" height="219" viewBox="0 0 251 219" role="img" aria-label="Heart-shaped collage: members praying together, volunteers with donated groceries, and a kitchen serving team">
    <defs>
      <clipPath id="heartClip"><path transform="translate(6.3 6) scale(.95)" d="M125.5 214C60 150 8 110 5 60C3 25 30 4 65 4C95 4 115 20 125.5 40C136 20 156 4 186 4C221 4 248 25 246 60C243 110 191 150 125.5 214Z"/></clipPath>
      <linearGradient id="p1" x1="0" y1="0" x2="1" y2="1"><stop offset="0" stop-color="#3a3436"/><stop offset="1" stop-color="#b99a8e"/></linearGradient>
      <linearGradient id="p2" x1="0" y1="0" x2="1" y2="1"><stop offset="0" stop-color="#c9b7a4"/><stop offset="1" stop-color="#5d6f94"/></linearGradient>
      <linearGradient id="p3" x1="0" y1="0" x2="1" y2="1"><stop offset="0" stop-color="#5c5752"/><stop offset="1" stop-color="#a9a39c"/></linearGradient>
    </defs>
    <g clip-path="url(#heartClip)">
      <rect x="0" y="0" width="122" height="112" fill="url(#p1)"/>
      <rect x="129" y="0" width="122" height="112" fill="url(#p2)"/>
      <rect x="0" y="119" width="251" height="100" fill="url(#p3)"/>
    </g>
    <path d="M125.5 214C60 150 8 110 5 60C3 25 30 4 65 4C95 4 115 20 125.5 40C136 20 156 4 186 4C221 4 248 25 246 60C243 110 191 150 125.5 214Z" fill="none" stroke="var(--red)" stroke-width="1.2"/>
  </svg>

  <div class="abs motto motto--love"><span class="script motto__word">Love</span><span class="motto__tail">like Him</span></div>
  <div class="abs motto-rule-v"></div>
  <div class="abs motto motto--live"><span class="script motto__word">Live</span><span class="motto__tail">like Him</span></div>
  <div class="abs motto-rule-h"></div>
  <div class="abs motto motto--lead"><span class="script motto__word">Lead</span><span class="motto__tail">like Him</span></div>

  <p class="abs site-front">www.brightwellchapel.org</p>
</section>

<!-- BACK PAGE -->
<section class="page page--back">
  <svg class="layer" width="524" height="678" viewBox="0 0 524 678" aria-hidden="true">
    <defs>
      <radialGradient id="mist2" cx="50%" cy="30%" r="70%"><stop offset="0" stop-color="#e4e4e4"/><stop offset="1" stop-color="#ffffff"/></radialGradient>
      <clipPath id="redZone"><path d="M0 0H524V352C470 332 420 326 360 332C280 342 220 400 140 405C80 408 30 395 0 380Z"/></clipPath>
    </defs>
    <rect width="524" height="678" fill="url(#mist2)"/>
    <path d="M0 380C30 395 80 412 140 409C220 404 280 346 360 336C420 330 470 336 524 356" fill="none" stroke="var(--red-bright)" stroke-width="3"/>
    <g clip-path="url(#redZone)">
      <rect width="524" height="420" fill="var(--red-deep)"/>
      <rect x="30" y="20" width="239" height="420" rx="30" fill="var(--red-panel)"/>
    </g>
  </svg>

  <p class="abs script kicker stories-kicker">Stories of</p>
  <h2 class="abs heading stories-title">What God Is Doing</h2>
  <div class="abs body-copy stories-copy">
    <p>One Wednesday night, a woman went to visit another church, but they were closed for a break. Instead of turning back, she came here. That unexpected moment became a divine appointment. God brought her to Brightwell.</p>
    <p>Another couple walked through our doors carrying deep church hurt. From the very first moment, they felt seen, valued, and welcomed. What they found here was not just a service, but a family.</p>
    <p>This is what we are building together.</p>
    <em>These gifts help build momentum, inspire others, and move the vision forward in powerful ways.</em>
  </div>
  <div class="abs dotted" style="top:230px"></div>
  <p class="abs join">JOIN US</p>
  <div class="abs dotted" style="top:278px"></div>

  <div class="abs practice" style="left:87px">
    <div class="practice__ring"><svg width="18" height="18" viewBox="0 0 18 18" fill="none" stroke="#fff" stroke-width="1.2"><path d="M9 16V7M9 7L6 2 4 9l3 5M9 7l3-5 2 7-3 5"/></svg></div>Pray</div>
  <div class="abs practice" style="left:132px">
    <div class="practice__ring"><svg width="18" height="18" viewBox="0 0 18 18" fill="none" stroke="#fff" stroke-width="1.2"><path d="M3 11V9a6 6 0 0 1 12 0v2"/><rect x="2" y="10" width="3" height="5" rx="1"/><rect x="13" y="10" width="3" height="5" rx="1"/></svg></div>Listen</div>
  <div class="abs practice" style="left:177px">
    <div class="practice__ring"><svg width="18" height="18" viewBox="0 0 18 18" fill="none" stroke="#fff" stroke-width="1.2"><path d="M9 15C5 12 3 10 3 7.5 3 5.5 4.5 4 6.2 4 7.5 4 8.5 5 9 6c.5-1 1.5-2 2.8-2C13.5 4 15 5.5 15 7.5 15 10 13 12 9 15Z"/><path d="M9 7.5v4M7.5 9h3"/></svg></div>Faith</div>

  <p class="abs belief">Together, we believe God will do more<br>than we can ask or imagine.</p>

  <p class="abs script kicker forward-kicker">How We</p>
  <h2 class="abs heading forward-title">Move Forward Together</h2>
  <div class="abs body-copy encourage">
    <b>We encourage</b>
    Everyone to participate, even one dollar a day matters<br>
    Some to give stretch gifts as they are able<br>
    A few to provide leadership gifts to help anchor the campaign
  </div>

  <p class="abs script kicker shared-kicker">A Shared</p>
  <h2 class="abs heading shared-title">Commitment</h2>
  <p class="abs body-copy shared-copy">“If each of us gave just $20 a week, we would not only meet our goal, we would exceed it. But this is not about equal giving. It is about equal sacrifice. Some can give more, some less, but together, we can do something powerful.”</p>

  <div class="abs seal seal--back"><div class="seal__inner">Brightwell<br>Chapel</div></div>

  <h2 class="abs model-title">Realistic Participation Model</h2>
  <p class="abs model-sub">Not everyone will give equally—so let’s build a real-world scenario:</p>
  <h3 class="abs tier-title">Tiered Giving Plan</h3>
  <table class="abs tiers">
    <colgroup><col class="c1"><col class="c2"><col class="c3"><col></colgroup>
    <thead><tr><th>Group</th><th>People</th><th>Weekly Gift</th><th>Yearly Total</th></tr></thead>
    <tbody>
      <tr><td>Leadership<br>Givers</td><td>10</td><td>$100</td><td>$52,000</td></tr>
      <tr><td>Core Givers</td><td>40</td><td>$40</td><td>$83,200</td></tr>
      <tr><td>Consistent<br>Givers</td><td>60</td><td>$20</td><td>$62,400</td></tr>
      <tr><td>Entry Givers</td><td>40</td><td>$10</td><td>$20,800</td></tr>
    </tbody>
  </table>

  <p class="abs total">Total: $218,400</p>
  <p class="abs total-note">This exceeds the goal, giving margin for:</p>
  <ul class="abs margins">
    <li>Missed weeks</li>
    <li>Lower participation</li>
    <li>Unexpected needs</li>
  </ul>
  <div class="abs rule-set"><span></span><span></span><span></span></div>
  <p class="abs site-back">www.brightwellchapel.org</p>
</section>
</body>
</html>
```